Letterhead Design for Law Firm that Specializes in Property Damage Litigation

We are looking for a redesign of our letterhead. Our current letterhead lists all of our current staff members and we'd like to come up with a design that does NOT list all of the staff members so that it does not need to be updated with every newly hired employee. Must be in editable format.

We are a law firm that specializes in property damage, so we need something that is professional, yet modern. The final design should use our existing logo and should use a blue color scheme (alternate colors would be gray, black, and white).

Industry/Entity Type

Legal

Colors
0054AA
0677BA
7BADD7
CADEEF
E8F1F8

```html
<!DOCTYPE html>
<html lang="en">
<head>
<meta charset="utf-8">
<title>Hartwell Ellery &amp; Langston – Letterhead</title>
<link href="https://fonts.googleapis.com/css2?family=Cinzel:wght@400;600&display=swap" rel="stylesheet">
<style>
  :root {
    --backdrop: #808185;
    --paper: #ffffff;
    --ink: #222222;
    --navy: #1f3a6e;
    --slate: #5e5f63;
    --rule: #3a3a3a;
    --mark-faint: #f0eff3;
  }
  * { margin: 0; padding: 0; box-sizing: border-box; }
  html, body {
    width: 1200px; height: 831px; overflow: hidden;
    background: var(--backdrop);
    font-family: "Cinzel", serif;
    color: var(--ink);
  }
  .canvas { position: relative; width: 1200px; height: 831px; }
  .sheet {
    position: absolute; top: 81px; width: 521px; height: 673px;
    background: var(--paper); overflow: hidden;
  }
  .sheet--plain { left: 68px; }
  .sheet--marked { left: 615px; }

  .faint-mark {
    position: absolute; left: 205px; top: 265px;
    width: 240px; height: 240px; background: var(--mark-faint);
  }

  .block { position: absolute; text-align: center; line-height: 9px; }
  .partners { left: 22px; width: 140px; top: 32px; }
  .partner-name { font-size: 8px; }
  .partner-mail { font-size: 6px; letter-spacing: .3px; color: #444; }
  .partner-rule { width: 46px; height: 1px; background: var(--rule); margin: 7px auto 7px; }

  .brand { left: 151px; width: 220px; top: 36px; }
  .brand-square { width: 10px; height: 10px; background: var(--navy); margin: 0 auto 8px; }
  .brand-name {
    font-size: 11px; font-weight: 600; color: var(--navy);
    line-height: 13px; letter-spacing: .3px; white-space: nowrap;
  }
  .brand-tag { font-size: 6px; letter-spacing: 1.2px; color: var(--slate); margin-top: 8px; }
  .brand-rule { width: 44px; height: 1px; background: var(--navy); margin: 5px auto 5px; }
  .brand-web { font-size: 7.5px; letter-spacing: .4px; }
  .brand-phone { font-size: 7px; }

  .offices { left: 360px; width: 140px; top: 34px; }
  .office-title { font-size: 7.5px; }
  .office-line { font-size: 6.5px; color: #333; }
  .office-line b { color: var(--navy); font-weight: 600; }
  .offices .gap { height: 14px; }

  .letter { position: absolute; left: 68px; width: 387px; font-size: 7.4px; line-height: 11px; }
  .recipient { top: 184px; }
  .subject { top: 240px; }
  .body { top: 273px; }
  .body p { text-align: justify; margin-bottom: 11px; }
  .closing { top: 471px; }
  .signature { top: 526px; }
</style>
</head>
<body>
<main class="canvas">

  <section class="sheet sheet--plain">
    <div class="block partners">
      <div class="partner-name">Daniel Hartwell, Esquire</div>
      <div class="partner-mail">dhartwell@helfirm.com</div>
      <div class="partner-rule"></div>
      <div class="partner-name">Marcus Ellery, Esquire</div>
      <div class="partner-mail">mellery@helfirm.com</div>
      <div class="partner-rule"></div>
      <div class="partner-name">Victor Langston, Esquire</div>
      <div class="partner-mail">vlangston@helfirm.com</div>
    </div>
    <div class="block brand">
      <div class="brand-square"></div>
      <div class="brand-name">Hartwell Ellery &amp; Langston</div>
      <div class="brand-tag">Property Loss Litigation Counsel</div>
      <div class="brand-rule"></div>
      <div class="brand-web">www.helfirm.com</div>
      <div class="brand-phone">(215) 555-0140</div>
    </div>
    <div class="block offices">
      <div class="office-title">Philadelphia Office</div>
      <div class="office-line"><b>T:</b> 215.555.0140</div>
      <div class="office-line"><b>T:</b> 215.555.0192</div>
      <div class="office-line">2240 Harbor Avenue</div>
      <div class="office-line">Suite 810</div>
      <div class="office-line">Riverton, PA 19107</div>
      <div class="gap"></div>
      <div class="office-title">New Jersey Office</div>
      <div class="office-line"><b>T:</b> 856.555.0127</div>
      <div class="office-line"><b>T:</b> 215.555.0192</div>
      <div class="office-line">375 Orchard Road</div>
      <div class="office-line">Suite 120</div>
      <div class="office-line">Maple Grove, NJ 08099</div>
    </div>
    <div class="letter recipient">lorem ipsum dolor sit<br>amet, consectetuer<br>adipiscing elit, sed diam</div>
    <div class="letter subject">nonummy nibh euismod tincidunt ut laoreet dolore</div>
    <div class="letter body">
      <p>magna aliquam erat volutpat. Ut wisi enim ad minim veniam, quis nostrud exerci tation ullamcorper suscipit lobortis nisl ut aliquip ex ea commodo consequat. Duis autem vel eum iriure dolor in hendrerit in vulputate velit esse molestie consequat, vel illum dolore eu feugiat nulla facilisis at vero eros et accumsan et iusto odio dignissim qui blandit praesent luptatum zzril delenit augue duis dolore te feugait nulla facilisi.</p>
      <p>Lorem ipsum dolor sit amet, cons ectetuer adipiscing elit, sed diam nonummy nibh euismod tincidunt ut laoreet dolore magna aliquam erat volutpat. Ut wisi enim ad minim veniam, quis nostrud exerci tation ullamcorper suscipit lobortis nisl ut aliquip ex ea commodo consequat.</p>
      <p>Lorem ipsum dolor sit amet, consectetuer adipiscing elit, sed diam nonummy nibh euismod tincidunt ut laoreet dolore magna aliquam erat volutpat. Ut wisi enim ad minim veniam, quis nostrud exerci tation ullamcorper suscipit lobortis nisl ut aliquip ex ea commodo consequat. Duis autem vel eum iriure dolor in hendrerit in vulputate velit esse molestie consequat, vel illum dolore eu feugiat nulla facilisis at vero eros et accumsan et iusto odio</p>
    </div>
    <div class="letter closing">dignissim qui blandi</div>
    <div class="letter signature">praesent luptatum zzril<br>delenit augue duis</div>
  </section>

  <section class="sheet sheet--marked">
    <div class="faint-mark"></div>
    <div class="block partners">
      <div class="partner-name">Daniel Hartwell, Esquire</div>
      <div class="partner-mail">dhartwell@helfirm.com</div>
      <div class="partner-rule"></div>
      <div class="partner-name">Marcus Ellery, Esquire</div>
      <div class="partner-mail">mellery@helfirm.com</div>
      <div class="partner-rule"></div>
      <div class="partner-name">Victor Langston, Esquire</div>
      <div class="partner-mail">vlangston@helfirm.com</div>
    </div>
    <div class="block brand">
      <div class="brand-square"></div>
      <div class="brand-name">Hartwell Ellery &amp; Langston</div>
      <div class="brand-tag">Property Loss Litigation Counsel</div>
      <div class="brand-rule"></div>
      <div class="brand-web">www.helfirm.com</div>
      <div class="brand-phone">(215) 555-0140</div>
    </div>
    <div class="block offices">
      <div class="office-title">Philadelphia Office</div>
      <div class="office-line"><b>T:</b> 215.555.0140</div>
      <div class="office-line"><b>T:</b> 215.555.0192</div>
      <div class="office-line">2240 Harbor Avenue</div>
      <div class="office-line">Suite 810</div>
      <div class="office-line">Riverton, PA 19107</div>
      <div class="gap"></div>
      <div class="office-title">New Jersey Office</div>
      <div class="office-line"><b>T:</b> 856.555.0127</div>
      <div class="office-line"><b>T:</b> 215.555.0192</div>
      <div class="office-line">375 Orchard Road</div>
      <div class="office-line">Suite 120</div>
      <div class="office-line">Maple Grove, NJ 08099</div>
    </div>
    <div class="letter recipient">lorem ipsum dolor sit<br>amet, consectetuer<br>adipiscing elit, sed diam</div>
    <div class="letter subject">nonummy nibh euismod tincidunt ut laoreet dolore</div>
    <div class="letter body">
      <p>magna aliquam erat volutpat. Ut wisi enim ad minim veniam, quis nostrud exerci tation ullamcorper suscipit lobortis nisl ut aliquip ex ea commodo consequat. Duis autem vel eum iriure dolor in hendrerit in vulputate velit esse molestie consequat, vel illum dolore eu feugiat nulla facilisis at vero eros et accumsan et iusto odio dignissim qui blandit praesent luptatum zzril delenit augue duis dolore te feugait nulla facilisi.</p>
      <p>Lorem ipsum dolor sit amet, cons ectetuer adipiscing elit, sed diam nonummy nibh euismod tincidunt ut laoreet dolore magna aliquam erat volutpat. Ut wisi enim ad minim veniam, quis nostrud exerci tation ullamcorper suscipit lobortis nisl ut aliquip ex ea commodo consequat.</p>
      <p>Lorem ipsum dolor sit amet, consectetuer adipiscing elit, sed diam nonummy nibh euismod tincidunt ut laoreet dolore magna aliquam erat volutpat. Ut wisi enim ad minim veniam, quis nostrud exerci tation ullamcorper suscipit lobortis nisl ut aliquip ex ea commodo consequat. Duis autem vel eum iriure dolor in hendrerit in vulputate velit esse molestie consequat, vel illum dolore eu feugiat nulla facilisis at vero eros et accumsan et iusto odio</p>
    </div>
    <div class="letter closing">dignissim qui blandi</div>
    <div class="letter signature">praesent luptatum zzril<br>delenit augue duis</div>
  </section>

</main>
</body>
</html>
```